Business Card/Letterhead Design

We have our Logo, we simply need it cleaned up. Along with a letterhead design. It's pretty simple really.
Instead of the "Corporation" beside the logo. We need it to say "Limited" just under the logo between the "F" and the "Y"
The letter head has to have our address. 4375 Calverton Road Lakeford, LK L4W 2K7 Westmark
Updates
Reason: I have been called out of town until Monday of next week.
Industry/Entity Type
Business
Contact Information for Business Card
4375 Calverton Road Lakeford, LK L4W 2K7 Westmark
Look and feel
Each slider illustrates characteristics of the customer's brand and the style your logo design should communicate.

```html
<!DOCTYPE html>
<html lang="en">
<head>
<meta charset="utf-8">
<title>Broadline Limited – Business Card</title>
<link rel="stylesheet" href="https://fonts.googleapis.com/css2?family=Cinzel:wght@400;500&display=swap">
<style>
  :root {
    --backdrop: #1c1c1e;
    --silver-dark: #8f9092;
    --silver-mid: #c9cacc;
    --silver-light: #eeeeef;
    --band-blue: #3a3fae;
    --band-blue-deep: #2c2f9a;
    --ink-blue: #2a2f9c;
    --rule-white: #f4f4f6;
    --accent-bronze: #b08a5e;
    --text-white: #ffffff;
  }
  * { margin: 0; padding: 0; box-sizing: border-box; }
  html, body {
    width: 1200px;
    height: 960px;
    overflow: hidden;
    background: var(--backdrop);
  }
  .canvas {
    position: relative;
    width: 1200px;
    height: 960px;
    display: flex;
    align-items: center;
    justify-content: center;
  }
  .business-card {
    position: relative;
    width: 900px;
    height: 514px;
    border-radius: 34px;
    overflow: hidden;
    background: linear-gradient(100deg,
      var(--silver-dark) 0%,
      var(--silver-mid) 28%,
      var(--silver-light) 50%,
      var(--silver-mid) 72%,
      var(--silver-dark) 100%);
  }
  .brand {
    position: absolute;
    left: 150px;
    top: 112px;
    display: flex;
    align-items: center;
    gap: 22px;
  }
  .brand-mark {
    width: 58px;
    height: 58px;
    border-radius: 50%;
    background: var(--accent-bronze);
  }
  .brand-name {
    font-family: "Cinzel", serif;
    font-weight: 500;
    font-size: 52px;
    letter-spacing: 2px;
    color: var(--ink-blue);
    line-height: 1;
  }
  .address-band {
    position: absolute;
    left: 0;
    right: 0;
    top: 258px;
    height: 142px;
    background: linear-gradient(90deg, var(--band-blue-deep), var(--band-blue));
    border-top: 4px solid var(--rule-white);
    border-bottom: 4px solid var(--rule-white);
    display: flex;
    align-items: center;
    justify-content: center;
  }
  .address {
    font-family: "Cinzel", serif;
    font-weight: 400;
    font-size: 27px;
    letter-spacing: 1.5px;
    color: var(--text-white);
    text-align: center;
    line-height: 1.25;
    font-style: normal;
  }
</style>
</head>
<body>
  <main class="canvas">
    <section class="business-card" aria-label="Broadline Limited business card">
      <div class="brand">
        <span class="brand-mark" aria-hidden="true"></span>
        <span class="brand-name">Broadline Limited</span>
      </div>
      <div class="address-band">
        <address class="address">
          4375 Calverton Road Lakeford,<br>
          LK L4W 2K7 Westmark
        </address>
      </div>
    </section>
  </main>
</body>
</html>
```